Ambo postcard design

I am in charge of getting a postcard 5x7 designed for 14 artists having a gallery exhibition. We would like to use our
photo(s) with the 14 names on the front. Back of card would have gallery information.
Am sending jpeg of a past card, four images to choose from and the text for back of card.

```html
<!DOCTYPE html>
<html lang="en">
<head>
<meta charset="utf-8">
<title>Fourteen Painters – Postcard</title>
<link rel="stylesheet" href="https://fonts.googleapis.com/css2?family=Open+Sans:wght@400;600;700&family=Lato:wght@400&display=swap">
<style>
  :root {
    --navy: #26304a;
    --ink: #2a3045;
    --grey-text: #6b6d72;
    --rule: #b9bcc2;
    --page: #eceae6;
    --white: #ffffff;
  }
  * { box-sizing: border-box; margin: 0; padding: 0; }
  html, body { width: 814px; height: 1200px; overflow: hidden; }
  body {
    background: var(--page);
    font-family: "Open Sans", Arial, sans-serif;
    position: relative;
  }
  .card {
    position: absolute;
    left: 51px;
    width: 712px;
    height: 512px;
    background: var(--white);
    overflow: hidden;
  }
  .card--front { top: 50px; }
  .card--back { top: 630px; }

  /* Front */
  .front-photo {
    position: absolute; left: 0; top: 0; width: 712px; height: 380px;
    background:
      linear-gradient(160deg, rgba(255,255,255,0.0) 30%, rgba(20,20,30,0.55) 75%),
      linear-gradient(115deg, #d9c9a4 0%, #e9e4d6 25%, #c7a15a 45%, #3c5e7c 62%, #e7d33b 78%, #c84a3a 100%);
  }
  .front-band { position: absolute; left: 0; top: 340px; width: 712px; height: 172px; }
  .front-title {
    position: absolute; left: 0; width: 100%; top: 398px;
    text-align: center; color: var(--white);
    font-family: "Lato", Arial, sans-serif;
    font-variant: small-caps; font-size: 30px; letter-spacing: 1px;
  }
  .front-names {
    position: absolute; left: 0; width: 100%; top: 444px;
    text-align: center; color: var(--white);
    font-size: 16.5px; line-height: 22px;
  }

  /* Back */
  .presenter {
    position: absolute; left: 30px; width: 324px; top: 26px;
    text-align: center;
  }
  .presenter__name { font-weight: 700; font-size: 21px; color: var(--ink); line-height: 30px; }
  .presenter__lead { font-size: 19px; color: var(--grey-text); line-height: 26px; }
  .group-title {
    position: absolute; left: 30px; width: 324px; top: 114px;
    text-align: center; color: var(--ink);
    font-weight: 700; font-variant: small-caps; font-size: 27px; letter-spacing: 0.5px;
  }
  .dates {
    position: absolute; left: 31px; width: 323px; top: 156px; height: 60px;
    border-top: 2px solid var(--navy); border-bottom: 2px solid var(--navy);
    text-align: center; color: var(--ink); font-size: 16.5px; line-height: 23px; padding-top: 6px;
  }
  .hours { position: absolute; left: 32px; top: 255px; font-size: 12.5px; line-height: 15px; color: var(--grey-text); }
  .hours__label { color: #222; }
  .parking { position: absolute; left: 32px; top: 316px; width: 350px; font-size: 12.5px; line-height: 15px; color: var(--grey-text); }
  .mailer {
    position: absolute; left: 355px; top: 28px; font-size: 10.5px; line-height: 16px; color: var(--grey-text);
  }
  .mailer__name { margin-bottom: 6px; }
  .stamp-box { position: absolute; left: 599px; top: 28px; width: 84px; height: 70px; border: 1.5px solid var(--rule); }
  .address-line { position: absolute; left: 448px; width: 234px; height: 0; border-top: 1.5px solid var(--rule); }
  .back-wave { position: absolute; left: 0; top: 380px; width: 712px; height: 132px; }
</style>
</head>
<body>

<section class="card card--front">
  <div class="front-photo" role="img" aria-label="Photograph of a wide paintbrush and palette knife resting on a canvas of colourful dripped paint"></div>
  <svg class="front-band" viewBox="0 0 712 172" aria-hidden="true">
    <path d="M0 30 Q180 -5 420 8 Q600 18 712 0 L712 172 L0 172 Z" fill="#d8d8dc"/>
    <path d="M0 38 Q200 5 430 16 Q600 24 712 8 L712 172 L0 172 Z" fill="#ffffff"/>
    <path d="M0 46 Q220 14 440 26 Q610 34 712 20 L712 172 L0 172 Z" fill="var(--navy)"/>
  </svg>
  <h1 class="front-title">Fourteen Painters</h1>
  <p class="front-names">
    Ashford ~ Brennick ~ Corwell ~ Dorsey ~ Ellis ~ Fairbanks ~ Garner ~ Holt<br>
    Ivers ~ Jessup ~ Kellan ~ Lorimer ~ Marsh ~ Norwood
  </p>
</section>

<section class="card card--back">
  <div class="presenter">
    <p class="presenter__name">Gallery Lowerlevel</p>
    <p class="presenter__lead">presents an exhibition by</p>
  </div>
  <h2 class="group-title">The Ambo Group</h2>
  <div class="dates">
    <p>September 28th – October 31, 2015</p>
    <p>Reception – Friday, October 2, 5-8pm</p>
  </div>
  <div class="hours">
    <p class="hours__label">Gallery Hours:</p>
    <p>M-F 10:00am-6:00pm</p>
    <p>Saturday 10:00am-2pm.</p>
  </div>
  <p class="parking">Parking is available in metered spots on nearby streets and in public garages (free on weekends and after 4pm weekdays)</p>

  <div class="mailer">
    <p class="mailer__name">Gallery Lowerlevel</p>
    <p>Harbor Point Shops, 4100 Linden Drive</p>
    <p>Fairview, Virginia 22999</p>
    <p>555-014-0652</p>
    <p>info@gallerylowerlevel.org</p>
    <p>www.gallerylowerlevel.org</p>
  </div>
  <div class="stamp-box"></div>
  <div class="address-line" style="top:170px"></div>
  <div class="address-line" style="top:199px"></div>
  <div class="address-line" style="top:228px"></div>
  <div class="address-line" style="top:257px"></div>
  <div class="address-line" style="top:286px"></div>

  <svg class="back-wave" viewBox="0 0 712 132" aria-hidden="true">
    <path d="M218 36 Q480 62 712 24 L712 30 Q480 70 218 36 Z" fill="var(--navy)"/>
    <path d="M0 48 Q130 28 300 44 Q520 64 712 2 L712 132 L0 132 Z" fill="var(--navy)"/>
    <path d="M218 36 Q470 72 712 30 L712 40 Q470 80 240 44 Z" fill="#ffffff"/>
  </svg>
</section>

</body>
</html>
```